Visitenkarte erstellen für Reiki Praxis

Visitenkarten für Reiki Praxis Doppelseitig

business cards reiki practice double-sided

The background can also be a different color

```html
<!DOCTYPE html>
<html lang="en">
<head>
<meta charset="utf-8">
<title>Quiet Harbor Reiki – Business Card</title>
<link rel="stylesheet" href="https://fonts.googleapis.com/css2?family=Open+Sans:wght@400;600&display=swap">
<style>
  :root {
    --canvas-bg: #b3b3b3;
    --card-light: #ffffff;
    --card-dark: #000000;
    --gold: #dda63a;
    --rose: #b95b86;
    --sage: #9a9e8f;
    --sand: #a99e8a;
    --ink: #3a3a3a;
    --brand-grey: #6b6b6b;
  }
  * { margin: 0; padding: 0; box-sizing: border-box; }
  html, body { width: 1001px; height: 1200px; overflow: hidden; }
  body {
    background: var(--canvas-bg);
    font-family: "Open Sans", Arial, sans-serif;
    position: relative;
  }
  .card {
    position: absolute;
    left: 51px;
    width: 899px;
    height: 541px;
    overflow: hidden;
  }
  .card--front { top: 42px; background: var(--card-light); }
  .card--back  { top: 616px; background: var(--card-dark); }
  .card__waves { position: absolute; inset: 0; width: 100%; height: 100%; }

  .brand {
    position: absolute;
    text-align: center;
    font-weight: 400;
    line-height: 1.15;
  }
  .brand__dot {
    display: block;
    margin: 0 auto 18px;
    border-radius: 50%;
    background: var(--gold);
  }
  .card--front .brand {
    left: 56px; width: 400px; top: 218px;
    color: var(--brand-grey);
    font-size: 33px;
  }
  .card--front .brand__dot { width: 44px; height: 44px; }
  .card--back .brand {
    left: 0; width: 899px; top: 196px;
    color: #ffffff;
    font-size: 44px;
  }
  .card--back .brand__dot { width: 56px; height: 56px; margin-bottom: 22px; }
  .brand__line { display: block; letter-spacing: 0.5px; }

  .contact {
    position: absolute;
    left: 507px;
    top: 140px;
    color: var(--ink);
  }
  .contact__name { font-size: 30px; font-weight: 600; line-height: 1.2; }
  .contact__role { font-size: 29px; font-weight: 400; line-height: 1.25; margin-bottom: 14px; }
  .contact__list { list-style: none; }
  .contact__item {
    display: flex;
    align-items: center;
    gap: 12px;
    height: 44px;
    font-size: 27px;
  }
  .contact__icon {
    width: 27px; height: 27px;
    background: var(--gold);
    border-radius: 3px;
    flex: none;
  }
</style>
</head>
<body>

<section class="card card--front">
  <svg class="card__waves" viewBox="0 0 1063 639" preserveAspectRatio="none" aria-hidden="true">
    <defs>
      <linearGradient id="band-front" x1="0" x2="1" y1="0" y2="0">
        <stop offset="0" stop-color="var(--sand)"/>
        <stop offset="0.15" stop-color="var(--sage)"/>
        <stop offset="1" stop-color="var(--rose)"/>
      </linearGradient>
    </defs>
    <path d="M0,0 H1063 V78 C950,35 850,25 740,25 C560,25 380,100 170,102 C100,103 40,92 0,80 Z" fill="url(#band-front)"/>
    <path d="M0,562 C120,600 260,614 400,612 C600,608 780,540 900,538 C980,537 1030,550 1063,560 V639 H0 Z" fill="var(--gold)"/>
  </svg>

  <div class="brand">
    <span class="brand__dot"></span>
    <span class="brand__line">QUIET HARBOR REIKI</span>
    <span class="brand__line">MARA VENN</span>
  </div>

  <div class="contact">
    <p class="contact__name">Your Name</p>
    <p class="contact__role">Manager</p>
    <ul class="contact__list">
      <li class="contact__item">
        <svg class="contact__icon" viewBox="0 0 27 27" aria-hidden="true"><rect width="27" height="27" rx="3" fill="var(--gold)"/><path d="M9 6 L12 10 L10.5 12 C11.5 14.5 13 16 15.5 17 L17 15.5 L21 18 L19 21 C13 21 7 15 7 8 Z" fill="none" stroke="#fff" stroke-width="1.6" stroke-linejoin="round"/></svg>
        <span>123 444 555</span>
      </li>
      <li class="contact__item">
        <svg class="contact__icon" viewBox="0 0 27 27" aria-hidden="true"><rect width="27" height="27" rx="3" fill="var(--gold)"/><path d="M13.5 21 C10 16 8.5 13.5 8.5 11 A5 5 0 0 1 18.5 11 C18.5 13.5 17 16 13.5 21 Z" fill="none" stroke="#fff" stroke-width="1.6"/><circle cx="13.5" cy="11" r="1.8" fill="#fff"/><line x1="9" y1="22.5" x2="18" y2="22.5" stroke="#fff" stroke-width="1.4"/></svg>
        <span>789 Your Street Here</span>
      </li>
      <li class="contact__item">
        <svg class="contact__icon" viewBox="0 0 27 27" aria-hidden="true"><rect width="27" height="27" rx="3" fill="var(--gold)"/><rect x="6" y="8" width="15" height="11" fill="none" stroke="#fff" stroke-width="1.5"/><path d="M6 8 L13.5 14.5 L21 8 M6 19 L11 13.5 M21 19 L16 13.5" fill="none" stroke="#fff" stroke-width="1.3"/></svg>
        <span>info@yourname.com</span>
      </li>
      <li class="contact__item">
        <svg class="contact__icon" viewBox="0 0 27 27" aria-hidden="true"><rect width="27" height="27" rx="3" fill="var(--gold)"/><circle cx="13.5" cy="13.5" r="7.5" fill="none" stroke="#fff" stroke-width="1.5"/><ellipse cx="13.5" cy="13.5" rx="3.2" ry="7.5" fill="none" stroke="#fff" stroke-width="1.3"/><line x1="6" y1="13.5" x2="21" y2="13.5" stroke="#fff" stroke-width="1.3"/></svg>
        <span>www.yourname.com</span>
      </li>
    </ul>
  </div>
</section>

<section class="card card--back">
  <svg class="card__waves" viewBox="0 0 1063 639" preserveAspectRatio="none" aria-hidden="true">
    <defs>
      <linearGradient id="band-back" x1="0" x2="1" y1="0" y2="0">
        <stop offset="0" stop-color="var(--rose)"/>
        <stop offset="0.85" stop-color="var(--sage)"/>
        <stop offset="1" stop-color="var(--sand)"/>
      </linearGradient>
    </defs>
    <g transform="translate(1063,0) scale(-1,1)">
      <path d="M0,0 H1063 V78 C950,35 850,25 740,25 C560,25 380,100 170,102 C100,103 40,92 0,80 Z" fill="url(#band-back)"/>
      <path d="M0,562 C120,600 260,614 400,612 C600,608 780,540 900,538 C980,537 1030,550 1063,560 V639 H0 Z" fill="var(--gold)"/>
    </g>
  </svg>

  <div class="brand">
    <span class="brand__dot"></span>
    <span class="brand__line">QUIET HARBOR REIKI</span>
    <span class="brand__line">MARA VENN</span>
  </div>
</section>

</body>
</html>
```